BrambleWorks business card

Looking for business card design that supports our company/software values. We have 2 logo designs at the moment but open to change if you think you can enhance the brand. Check out website www.brambleworks.com.au.

Target Market(s)

Education

Contact Information for Business Card

Name, title, mobile, email and website

Font styles to use
Sans Serif

Colors

Designer to choose colors to be used in the design.

Requirements
Must have
• BrambleWorks logo with tree and tagline on rear side with dark grey background colour

```html
<!DOCTYPE html>
<html lang="en">
<head>
<meta charset="utf-8">
<title>BrambleWorks business card</title>
<link rel="stylesheet" href="https://fonts.googleapis.com/css2?family=Raleway:wght@400;500;600;700&display=swap">
<style>
  :root {
    --backdrop: #dcdcdc;
    --card: #ffffff;
    --ink: #555555;
    --ink-soft: #5f5f5f;
    --accent: #5b8c2a;
    --rule: #8a8a8a;
  }
  * { box-sizing: border-box; margin: 0; padding: 0; }
  html, body {
    width: 1200px;
    height: 1200px;
    overflow: hidden;
    background: var(--backdrop);
    font-family: "Raleway", Arial, sans-serif;
    color: var(--ink);
  }
  .card {
    position: absolute;
    left: 257px;
    width: 686px;
    height: 392px;
    background: var(--card);
  }
  .card--front { top: 165px; }
  .card--back { top: 653px; }

  .holder {
    position: absolute;
    right: 381px;
    top: 170px;
    text-align: right;
  }
  .holder__name {
    font-size: 23px;
    font-weight: 700;
    color: var(--ink);
    letter-spacing: 0.2px;
  }
  .holder__title {
    font-size: 16px;
    font-weight: 500;
    color: var(--accent);
    margin-top: 2px;
  }
  .divider {
    position: absolute;
    left: 322px;
    top: 143px;
    width: 1.5px;
    height: 103px;
    background: var(--rule);
  }
  .contacts {
    position: absolute;
    left: 341px;
    top: 149px;
    list-style: none;
  }
  .contacts li {
    display: flex;
    align-items: center;
    height: 19.5px;
    font-size: 16px;
    color: var(--ink-soft);
  }
  .contacts svg {
    width: 13px;
    height: 13px;
    margin-right: 9px;
    fill: var(--ink);
    flex: none;
  }
  .address {
    position: absolute;
    left: 161px;
    top: 330px;
    display: flex;
    align-items: center;
    font-size: 16px;
    color: var(--ink-soft);
  }
  .address svg {
    width: 14px;
    height: 18px;
    margin-right: 7px;
    fill: var(--ink);
  }

  .brand {
    position: absolute;
    left: 175px;
    top: 150px;
    display: flex;
    align-items: center;
  }
  .brand__dot {
    width: 78px;
    height: 78px;
    border-radius: 50%;
    background: var(--accent);
    margin-right: 22px;
  }
  .brand__text { display: flex; flex-direction: column; }
  .brand__name {
    font-size: 42px;
    font-weight: 500;
    color: var(--ink);
    line-height: 1;
    padding-bottom: 8px;
    border-bottom: 1.5px solid var(--rule);
  }
  .brand__tagline {
    font-size: 19px;
    font-weight: 500;
    color: var(--ink);
    margin-top: 6px;
    padding-left: 6px;
  }
</style>
</head>
<body>
  <section class="card card--front" aria-label="Card front">
    <div class="holder">
      <div class="holder__name">Daniel Hart</div>
      <div class="holder__title">President</div>
    </div>
    <div class="divider"></div>
    <ul class="contacts">
      <li><svg viewBox="0 0 16 16" aria-hidden="true"><path d="M3.5 1l2.5 3-1.5 2a9 9 0 0 0 5 5l2-1.5 3 2.5-1.5 3C6 15 1 10 .5 2.5z"/></svg>412-208-7731</li>
      <li><svg viewBox="0 0 16 16" aria-hidden="true"><path d="M4 0h8a1 1 0 0 1 1 1v14a1 1 0 0 1-1 1H4a1 1 0 0 1-1-1V1a1 1 0 0 1 1-1zm1 2v10h6V2zm3 11a1 1 0 1 0 0 2 1 1 0 0 0 0-2z"/></svg>412-590-3346</li>
      <li><svg viewBox="0 0 16 16" aria-hidden="true"><path d="M4 1h8v4H4zM1 6h14v6h-2v3H3v-3H1zm4 4v3h6v-3z"/></svg>412-377-1904</li>
      <li><svg viewBox="0 0 16 16" aria-hidden="true"><path d="M1 3h14v10H1zm1.5 1.5L8 9l5.5-4.5z"/></svg>info@brambleworks.com.au</li>
      <li><svg viewBox="0 0 16 16" aria-hidden="true"><path d="M8 1a7 7 0 1 0 0 14A7 7 0 0 0 8 1zm-2 3.5 2.5.5.5 2-2 1.5L5 11l-1-3 1-2zm5 5 1.5.5-1 2.5-1.5-1z"/></svg>www.brambleworks.com.au</li>
    </ul>
    <div class="address">
      <svg viewBox="0 0 14 18" aria-hidden="true"><path d="M7 0a6.5 6.5 0 0 0-6.5 6.5C.5 11.5 7 18 7 18s6.5-6.5 6.5-11.5A6.5 6.5 0 0 0 7 0zm0 3.5a3 3 0 1 1 0 6 3 3 0 0 1 0-6z"/></svg>
      2140 Alder Court, Juneau, Alaska 34512
    </div>
  </section>

  <section class="card card--back" aria-label="Card back">
    <div class="brand">
      <div class="brand__dot"></div>
      <div class="brand__text">
        <div class="brand__name">BrambleWorks</div>
        <div class="brand__tagline">Student Success Platform</div>
      </div>
    </div>
  </section>
</body>
</html>
```